Urgent seeking Cover Design for event

An Outdoor Movie Event company in singapore is seeking for a Cover Design to be placed on Lumoket for an outdoor movie event at a location called Marrowgate Plaza.
Cover design size is 920px by 450px
We have provided images in this project for your side to come out with something suitable but not too complicated.
We urgently need the design which can be in PDF format for easy editing on our ends. We also need all readable and editable working files.

Target Market(s)

movie goers

Colors

Designer to choose colors to be used in the design.

Requirements
Must have
• Simple design to incorporate images provided if able to.
Nice to have
• Cover size to be 920px by 450px
Should not have
• Not be too messy

```html
<!DOCTYPE html>
<html lang="en">
<head>
<meta charset="utf-8">
<title>Outdoor Movie Night Cover</title>
<link rel="stylesheet" href="https://fonts.googleapis.com/css2?family=Roboto+Condensed:wght@700&family=Questrial&display=swap">
<style>
  :root {
    --sky-top: #3d64b8;
    --sky-mid: #6f8fc4;
    --tree: #1f3a22;
    --lawn: #3f7a2c;
    --lawn-dark: #2c5a1f;
    --brand-red: #5e0d14;
    --panel: rgba(58, 58, 58, 0.62);
    --white: #ffffff;
    --page: #ffffff;
  }
  * { margin: 0; padding: 0; box-sizing: border-box; }
  html, body { width: 1200px; height: 554px; overflow: hidden; background: var(--page); }
  .cover { position: relative; width: 1200px; height: 554px; }
  .event-photo {
    position: absolute; left: 0; top: 0; width: 1127px; height: 554px;
    background: linear-gradient(180deg, var(--sky-top) 0%, var(--sky-mid) 30%, var(--tree) 45%, var(--tree) 55%, var(--lawn) 68%, var(--lawn-dark) 100%);
  }
  .brand-band {
    position: absolute; left: 643px; top: 59px; width: 457px; height: 106px;
    background: var(--brand-red); color: var(--white);
    display: flex; flex-direction: column; align-items: center; justify-content: center;
    font-family: "Questrial", sans-serif;
  }
  .brand-name { font-size: 52px; letter-spacing: 2px; line-height: 1; text-transform: uppercase; }
  .brand-legal { font-size: 12.5px; letter-spacing: 1.5px; margin-top: 6px; text-transform: uppercase; }
  .info-panel {
    position: absolute; left: 643px; top: 175px; width: 457px; height: 292px;
    background: var(--panel); color: var(--white);
  }
  .headline {
    position: absolute; left: 17px; top: 18px; width: 432px;
    font-family: "Roboto Condensed", sans-serif; font-weight: 700;
    font-size: 40px; line-height: 1; white-space: nowrap; letter-spacing: 0.2px;
  }
  .summary {
    position: absolute; left: 34px; top: 96px; width: 393px;
    font-family: "Questrial", sans-serif; font-size: 20px; line-height: 23.5px;
    text-align: justify; text-align-last: justify;
  }
  .social-links { position: absolute; left: 159px; top: 227px; display: flex; gap: 12px; }
  .social-dot { width: 40px; height: 40px; border-radius: 50%; background: var(--white); }
</style>
</head>
<body>
<main class="cover">
  <div class="event-photo" role="img" aria-label="Evening outdoor movie screening on a park lawn with an inflatable screen, trees, a pond and guests on picnic mats"></div>

  <header class="brand-band">
    <div class="brand-name">Lanceray</div>
    <div class="brand-legal">Lanceray Events Pte Ltd</div>
  </header>

  <section class="info-panel">
    <h1 class="headline">LOREM IPSUM DOLOR SIT</h1>
    <p class="summary">Lorem ipsum dolor sit amet, consec&shy;tetuer adipiscing elit, sed diam nonum&shy;my nibh euismod tincidunt ut laoreet dolore magna aliquam erat volutpat. Ut wisi enim ad minim veniam, quis nostrud</p>
    <div class="social-links">
      <span class="social-dot" role="img" aria-label="Social link"></span>
      <span class="social-dot" role="img" aria-label="Social link"></span>
      <span class="social-dot" role="img" aria-label="Social link"></span>
    </div>
  </section>
</main>
</body>
</html>
```